Powerpoint template & style design project

KMaldrey Consulting is an IT technology firm specializing in mobility and telecommunications applications. We provide technical consulting to global companies that want to build mobile applications and take critical business applications and move them into the cloud.
We would like to see designs that use the color blue. The final design should communicate confidence, agility and speak to technology focused customers. Forward progress and/or motion should be conveyed.

Target Market(s)

Government customers and large enterprise companies

Industry/Entity Type

Telecommunications

Font styles to use
Sans Serif

Colors
0555a3

Requirements
Must have
• different slides: Cover page, title slide, main content, transition slide, close out slide..

```html
<!DOCTYPE html>
<html lang="en">
<head>
<meta charset="utf-8">
<title>KMaldrey Consulting – Presentation Template</title>
<link href="https://fonts.googleapis.com/css2?family=Roboto:ital,wght@0,300;0,400;0,700;1,400&family=Roboto+Condensed:wght@700&display=swap" rel="stylesheet">
<style>
:root{
  --blue:#0555a3;
  --blue-dark:#0a3f7e;
  --navy:#0b1f4a;
  --sky:#1f8fd8;
  --grey:#9a9a9a;
  --grey-light:#c4c4c4;
  --charcoal:#444446;
  --text:#555;
  --bg:#e6e6e6;
  --white:#fff;
}
*{box-sizing:border-box;margin:0;padding:0}
html,body{width:1200px;height:907px;overflow:hidden;background:var(--bg);font-family:"Roboto",Arial,sans-serif;color:var(--text)}
.board{position:relative;width:1200px;height:907px}
.slide{position:absolute;width:357px;height:276px;background:var(--white);overflow:hidden}
.c1{left:45px}.c2{left:414px}.c3{left:784px}
.r1{top:30px}.r2{top:314px}.r3{top:603px}
.abs{position:absolute}
.title{position:absolute;left:14px;right:14px;top:18px;font-weight:300;font-size:13px;color:var(--blue);border-bottom:1px solid #9ab;line-height:14px;padding-bottom:1px}
.footer{position:absolute;left:0;bottom:0;width:357px;height:30px}
.foot-note{position:absolute;bottom:7px;left:6px;font-size:3.6px;color:#fff}
.foot-page{position:absolute;bottom:7px;left:176px;font-size:3.6px;color:#fff}
.brand{position:absolute;color:#fff;font-family:"Roboto",Arial,sans-serif;font-weight:400;line-height:1;white-space:nowrap}
.foot-brand{right:10px;bottom:8px;font-size:6px}
.para{font-size:5px;line-height:7.6px;text-align:justify}
.ph{position:absolute}
/* cover */
.cover-top{position:absolute;top:0;left:0;width:100%;height:3px;background:var(--blue)}
.cover-head{left:35px;top:40px;font-weight:300;font-size:15px;line-height:17.5px;color:var(--blue)}
.cover-date{left:35px;top:79px;font-size:6.5px;color:#333}
.cover-brand{right:20px;bottom:26px;font-size:12px}
/* about */
.about-lead{left:14px;top:135px;width:100px;font-size:5px;line-height:9.3px;color:var(--blue);text-transform:uppercase}
.about-body{left:134px;top:132px;width:206px}
.band{left:0;right:0;top:50px;height:69px;background:var(--charcoal)}
.band-text{left:130px;top:70px;width:200px;font-size:5.2px;line-height:12.5px;font-style:italic;color:#fff}
.about2-body{left:130px;top:127px;width:196px;font-size:4.3px;line-height:6.1px}
.about2-body p{margin-bottom:5px}
/* charts */
.legend{top:208px;width:90px;font-size:4px;line-height:5px}
.legend b{display:block;font-weight:400;font-size:4.6px;color:#333;margin-bottom:2px}
.legend i{display:inline-block;width:5px;height:5px;margin-right:6px;vertical-align:-1px}
.stat{top:140px;width:96px;text-align:center}
.stat strong{display:block;font-family:"Roboto Condensed",Arial,sans-serif;font-size:11px;color:var(--blue);margin-bottom:6px}
.stat span{display:block;font-size:4.3px;line-height:5.8px;color:#888}
/* team */
.team-intro{left:20px;right:20px;top:49px;text-align:center;font-size:4.5px;line-height:9.5px;font-style:italic;font-weight:700;color:#333}
.member{top:144px;width:80px}
.member h3{text-align:center;font-weight:400;font-size:5.5px;color:var(--blue)}
.member h4{text-align:center;font-weight:400;font-style:italic;font-size:3.8px;color:#333;margin-bottom:8px}
.member p{font-size:4.3px;line-height:10px;color:#999;text-align:justify}
/* image text */
.panel{left:0;top:0;width:183px;height:276px;background:var(--blue)}
.panel-title{left:14px;top:16px;font-weight:300;font-size:13px;color:#fff}
.panel-lead{left:30px;top:100px;font-size:5px;color:#fff}
.panel-body{left:30px;top:113px;width:132px;color:#fff;font-size:4.6px;line-height:7.1px;text-align:justify}
.panel-body p{margin-bottom:6px}
.panel-brand{left:18px;bottom:16px;font-size:6px}
/* section */
.section{background:linear-gradient(160deg,#1b74c4 0%,#0d5cab 45%,#0a4a93 100%)}
.section-title{left:0;right:0;top:176px;text-align:center;font-weight:300;font-size:12px;color:#fff}
/* close */
.close-brand{left:31px;top:60px;font-size:13px;color:var(--blue)}
.contact{font-size:5.6px;color:#fff;line-height:6.4px}
.socials{display:flex;gap:3px}
.socials span{width:9px;height:9px;border-radius:2px;background:#fff}
</style>
</head>
<body>
<main class="board">

<!-- Cover -->
<section class="slide c1 r1">
  <div class="cover-top"></div>
  <h1 class="abs cover-head">WELCOME<br>TO OUR PRESENTATION</h1>
  <p class="abs cover-date">Birmingham, March 25, 2011</p>
  <div class="ph" role="img" aria-label="Technology photo of a hand touching a glowing hexagon interface" style="left:0;top:99px;width:357px;height:101px;background:linear-gradient(120deg,#0b4b93 0%,#3f9be0 40%,#8cc8f2 60%,#2a7bd0 100%)"></div>
  <svg class="abs" style="left:0;top:184px" width="357" height="92" viewBox="0 0 357 92">
    <polygon points="210,0 357,0 357,16 196,16" fill="var(--grey)"/>
    <rect y="16" width="357" height="76" fill="var(--blue)"/>
  </svg>
  <div class="brand cover-brand">KMaldrey Consulting</div>
</section>

<!-- About 1 -->
<section class="slide c2 r1">
  <h2 class="title">ABOUT US</h2>
  <div class="ph" role="img" aria-label="Black and white photo of a smiling business team at a table" style="left:14px;top:38px;width:327px;height:76px;background:linear-gradient(90deg,#8d8d8d,#d5d5d5 50%,#9a9a9a)"></div>
  <p class="abs about-lead">Lorem ipsum dolor sit met consectur adipiscing elit, sed do euismod tempor incididunt ut labore et delore magna</p>
  <div class="abs about-body para">
    <p style="margin-bottom:8px">Lorem ipsum dolor sit amet, consectetur adipisicing elit, sed do eiusmod tempor incididunt ut labore et dolore magna aliqua. Ut enim ad minim veniam, quis nostrud exercitation ullamco laboris nisi ut aliquip ex ea commodo consequat. Duis aute irure dolor in reprehenderit in voluptate velit esse cillum dolore eu fugiat nulla pariatur.</p>
    <p>Lorem ipsum dolor sit amet, consectetur adipisicing elit, sed do eiusmod tempor incididunt ut labore et dolore magna aliqua. Ut enim ad minim veniam, quis nostrud exercitation ullamco laboris nisi ut aliquip ex ea commodo consequat. Duis aute irure dolor in reprehenderit in voluptate velit esse cillum dolore eu</p>
  </div>
  <svg class="footer" viewBox="0 0 357 30"><polygon points="0,0 230,0 222,8 0,8" fill="var(--grey)"/><polygon points="230,0 290,0 282,8 222,8" fill="var(--sky)"/><rect y="8" width="357" height="22" fill="var(--blue)"/></svg>
  <span class="foot-note">Proprietary and Confidential to KMaldrey Consulting</span><span class="foot-page">10</span>
  <div class="brand foot-brand">KMaldrey Consulting</div>
</section>

<!-- About 2 -->
<section class="slide c3 r1">
  <h2 class="title">ABOUT US</h2>
  <div class="abs band"></div>
  <div class="ph" role="img" aria-label="Black and white photo of a businesswoman in an office" style="left:0;top:48px;width:108px;height:73px;background:linear-gradient(90deg,#6d6d6d,#cfcfcf)"></div>
  <p class="abs band-text">Lorem ipsum dolor sit amet<br>consectetur adipisicing elit, sed do eiusmod tempor incididunt ut<br>labore et dolore magna aliqua. Ut enim ad minim veniam, quis</p>
  <div class="abs about2-body">
    <p>Lorem ipsum dolor sit amet, consectetur adipisicing elit, sed do eiusmod tempor incididunt ut labore et dolore magna aliqua. Ut enim ad minim veniam, quis nostrud exercitation ullamco laboris nisi ut aliquip ex ea commodo consequat. Duis aute irure dolor in reprehenderit in voluptate velit esse cillum dolore eu fugiat nulla pariatur.</p>
    <p>Lorem ipsum dolor sit amet, consectetur adipisicing elit, sed do eiusmod tempor incididunt ut labore et dolore magna aliqua. Ut enim ad minim veniam, quis nostrud exercitation ullamco laboris nisi ut aliquip ex ea commodo consequat. Duis aute irure dolor in reprehenderit in voluptate velit esse cillum dolore eu.</p>
    <p>Fugiat nulla pariatur. Excepteur sint occaecat cupidatat non proident, sunt in culpa qui officia deserunt mollit anim id est laborum. Excepteur sint occaecat cupidatat non proident, sunt in consequat. Duis aute irure dolor in reprehenderit in voluptate velit esse cillum dolore eu</p>
  </div>
  <svg class="footer" viewBox="0 0 357 30"><polygon points="0,0 230,0 222,8 0,8" fill="var(--grey)"/><polygon points="230,0 290,0 282,8 222,8" fill="var(--sky)"/><rect y="8" width="357" height="22" fill="var(--blue)"/></svg>
  <span class="foot-note">Proprietary and Confidential to KMaldrey Consulting</span><span class="foot-page">10</span>
  <div class="brand foot-brand">KMaldrey Consulting</div>
</section>

<!-- Chart: bars -->
<section class="slide c1 r2">
  <h2 class="title">OUR CHART</h2>
  <svg class="abs" style="left:0;top:0" width="357" height="200" viewBox="0 0 357 200" font-family="Roboto,Arial,sans-serif">
    <g stroke="#777" stroke-width=".6">
      <line x1="74" y1="48" x2="74" y2="166"/>
      <line x1="71" y1="48" x2="74" y2="48"/><line x1="71" y1="68" x2="74" y2="68"/><line x1="71" y1="87" x2="74" y2="87"/><line x1="71" y1="107" x2="74" y2="107"/><line x1="71" y1="126" x2="74" y2="126"/><line x1="71" y1="146" x2="74" y2="146"/>
      <line x1="74" y1="166" x2="290" y2="166"/>
    </g>
    <rect x="80" y="79" width="12" height="87" fill="var(--blue)"/><rect x="92" y="118" width="12" height="48" fill="var(--grey-light)"/><rect x="104" y="126" width="12" height="40" fill="var(--navy)"/>
    <rect x="130" y="103" width="12" height="63" fill="var(--blue)"/><rect x="142" y="80" width="12" height="86" fill="var(--grey-light)"/><rect x="154" y="126" width="12" height="40" fill="var(--navy)"/>
    <rect x="180" y="88" width="12" height="78" fill="var(--blue)"/><rect x="192" y="127" width="12" height="39" fill="var(--grey-light)"/><rect x="204" y="110" width="12" height="56" fill="var(--navy)"/>
    <rect x="230" y="91" width="12" height="75" fill="var(--blue)"/><rect x="242" y="119" width="12" height="47" fill="var(--grey-light)"/><rect x="254" y="83" width="12" height="83" fill="var(--navy)"/>
    <rect x="142" y="66" width="12" height="7" fill="var(--grey-light)"/><text x="148" y="71" font-size="3.5" fill="#fff" text-anchor="middle">72%</text>
    <rect x="180" y="75" width="12" height="7" fill="var(--blue)"/><text x="186" y="80" font-size="3.5" fill="#fff" text-anchor="middle">65%</text>
    <rect x="204" y="98" width="12" height="7" fill="var(--navy)"/><text x="210" y="103" font-size="3.5" fill="#fff" text-anchor="middle">43%</text>
    <g font-size="8" fill="#555" text-anchor="middle"><text x="98" y="181">2009</text><text x="148" y="181">2010</text><text x="198" y="181">2011</text><text x="248" y="181">2012</text></g>
  </svg>
  <div class="abs legend" style="left:45px"><b><i style="background:var(--blue)"></i>LOREM IPSUM</b><span style="display:block;padding-left:11px">Lorem ipsum dolor sit amet, consectetur adipisicing elit, sed do eiusmod tempor incididunt ut labore et dolore magna</span></div>
  <div class="abs legend" style="left:138px"><b><i style="background:var(--grey-light)"></i>LOREM IPSUM</b><span style="display:block;padding-left:11px">Lorem ipsum dolor sit amet, consectetur adipisicing elit, sed do eiusmod tempor incididunt ut labore et dolore magna</span></div>
  <div class="abs legend" style="left:233px"><b><i style="background:var(--navy)"></i>LOREM IPSUM</b><span style="display:block;padding-left:11px">Lorem ipsum dolor sit amet, consectetur adipisicing elit, sed do eiusmod tempor incididunt ut labore et dolore magna</span></div>
  <svg class="footer" viewBox="0 0 357 30"><polygon points="0,0 230,0 222,8 0,8" fill="var(--grey)"/><polygon points="230,0 290,0 282,8 222,8" fill="var(--sky)"/><rect y="8" width="357" height="22" fill="var(--blue)"/></svg>
  <span class="foot-note">Proprietary and Confidential to KMaldrey Consulting</span><span class="foot-page">10</span>
  <div class="brand foot-brand">KMaldrey Consulting</div>
</section>

<!-- Chart: donuts -->
<section class="slide c2 r2">
  <h2 class="title">OUR CHART</h2>
  <svg class="abs" style="left:0;top:70px" width="357" height="66" viewBox="0 0 357 66">
    <circle cx="63" cy="33" r="25" fill="none" stroke="var(--grey)" stroke-width="6"/>
    <circle cx="63" cy="33" r="25" fill="none" stroke="var(--blue)" stroke-width="6" stroke-dasharray="127 157" transform="rotate(-90 63 33)"/>
    <circle cx="63" cy="33" r="18" fill="none" stroke="var(--blue)" stroke-width="1"/>
    <g fill="var(--blue)"><circle cx="63" cy="33" r="7"/><circle cx="63" cy="33" r="2.5" fill="#fff"/></g>
    <circle cx="182" cy="33" r="25" fill="none" stroke="var(--grey)" stroke-width="6"/>
    <circle cx="182" cy="33" r="25" fill="none" stroke="var(--navy)" stroke-width="6" stroke-dasharray="113 157" transform="rotate(-90 182 33)"/>
    <circle cx="182" cy="33" r="18" fill="none" stroke="var(--blue)" stroke-width="1"/>
    <g fill="var(--blue)"><rect x="175" y="33" width="3" height="7"/><rect x="180" y="30" width="3" height="10"/><rect x="185" y="27" width="3" height="13"/><path d="M174 30 L181 24 L185 26 L189 22" stroke="var(--blue)" stroke-width="1.5" fill="none"/></g>
    <circle cx="294" cy="33" r="25" fill="none" stroke="var(--grey)" stroke-width="6"/>
    <circle cx="294" cy="33" r="25" fill="none" stroke="var(--navy)" stroke-width="6" stroke-dasharray="99 157" transform="rotate(-90 294 33)"/>
    <circle cx="294" cy="33" r="18" fill="none" stroke="var(--blue)" stroke-width="1"/>
    <g fill="none" stroke="var(--blue)" stroke-width="1.4"><rect x="287" y="26" width="14" height="10"/><line x1="294" y1="36" x2="294" y2="40"/><line x1="290" y1="40" x2="298" y2="40"/></g>
  </svg>
  <div class="abs stat" style="left:15px"><strong>81%</strong><span>dolor sit amet, consectetur adipisicing elit, sed do eiusmod tempor incididunt ut labore et dolore magna aliqua. Ut enim ad minim veniam, quis nostrud exercitation ullamco laboris nisi ut aliquip ex ea cesse cillum dolore eu fugiat nulla pariatur.</span></div>
  <div class="abs stat" style="left:134px"><strong>72%</strong><span>dolor sit amet, consectetur adipisicing elit, sed do eiusmod tempor incididunt ut labore et dolore magna aliqua. Ut enim ad minim veniam, quis nostrud exercitation ullamco laboris nisi ut aliquip ex ea cesse cillum dolore eu fugiat nulla pariatur.</span></div>
  <div class="abs stat" style="left:246px"><strong>63%</strong><span>dolor sit amet, consectetur adipisicing elit, sed do eiusmod tempor incididunt ut labore et dolore magna aliqua. Ut enim ad minim veniam, quis nostrud exercitation ullamco laboris nisi ut aliquip ex ea cesse cillum dolore eu fugiat nulla pariatur.</span></div>
  <svg class="footer" viewBox="0 0 357 30"><polygon points="0,0 230,0 222,8 0,8" fill="var(--grey)"/><polygon points="230,0 290,0 282,8 222,8" fill="var(--sky)"/><rect y="8" width="357" height="22" fill="var(--blue)"/></svg>
  <span class="foot-note">Proprietary and Confidential to KMaldrey Consulting</span><span class="foot-page">10</span>
  <div class="brand foot-brand">KMaldrey Consulting</div>
</section>

<!-- Team -->
<section class="slide c3 r2">
  <h2 class="title">OUR TEAM</h2>
  <p class="abs team-intro">dolor sit amet, consectetur adipisicing elit, sed do eiusmod tempor incididunt ut labore et dolore magna aliqua.<br>Ut enim ad minim veniam, quis nostrud exercitation ullamco laboris nisi ut a</p>
  <div class="ph" role="img" aria-label="Portrait photo of team member" style="left:40px;top:84px;width:52px;height:52px;border-radius:50%;border:1px solid var(--blue);background:radial-gradient(circle at 50% 40%,#d8d8d8,#7a7a7a)"></div>
  <div class="ph" role="img" aria-label="Portrait photo of team member" style="left:150px;top:84px;width:52px;height:52px;border-radius:50%;border:1px solid var(--blue);background:radial-gradient(circle at 50% 40%,#e0e0e0,#8a8a8a)"></div>
  <div class="ph" role="img" aria-label="Portrait photo of team member" style="left:256px;top:84px;width:52px;height:52px;border-radius:50%;border:1px solid var(--blue);background:radial-gradient(circle at 50% 40%,#ececec,#9a9a9a)"></div>
  <div class="abs member" style="left:26px"><h3>JORDAN VALE</h3><h4>President</h4><p>dolor sit amet, consectetur adipiscing elit, sed do eiusmod tempor incididunt ut labore et dolore magna aliqua. Ut enim ad minim veniam, quis nostrud exercitation</p></div>
  <div class="abs member" style="left:136px"><h3>MIRA CASTELL</h3><h4>CEO / Founder</h4><p>dolor sit amet, consectetur adipiscing elit, sed do eiusmod tempor incididunt ut labore et dolore magna aliqua. Ut enim ad minim veniam, quis nostrud exercitation</p></div>
  <div class="abs member" style="left:242px"><h3>NORA LINDEN</h3><h4>Vice President</h4><p>dolor sit amet, consectetur adipiscing elit, sed do eiusmod tempor incididunt ut labore et dolore magna aliqua. Ut enim ad minim veniam, quis nostrud exercitation</p></div>
  <svg class="footer" viewBox="0 0 357 30"><polygon points="0,0 230,0 222,8 0,8" fill="var(--grey)"/><polygon points="230,0 290,0 282,8 222,8" fill="var(--sky)"/><rect y="8" width="357" height="22" fill="var(--blue)"/></svg>
  <span class="foot-note">Proprietary and Confidential to KMaldrey Consulting</span><span class="foot-page">10</span>
  <div class="brand foot-brand">KMaldrey Consulting</div>
</section>

<!-- Image text -->
<section class="slide c1 r3">
  <div class="abs panel"></div>
  <div class="ph" role="img" aria-label="Black and white photo of a smiling businesswoman and businessman" style="left:183px;top:0;width:174px;height:276px;background:linear-gradient(160deg,#e9e9e9 0%,#a5a5a5 55%,#4a4a4a 100%)"></div>
  <h2 class="abs panel-title">IMAGE TEXT</h2>
  <p class="abs panel-lead">LOREM IPSUM DOLOR SIT MET</p>
  <div class="abs panel-body">
    <p>Lorem ipsum dolor sit amet, consectetur adipisicing elit, sed do eiusmod tempor incididunt ut labore et dolore magna aliqua. Ut enim ad minim veniam, quis nostrud exercitation ullamco laboris nisi ut aliquip ex ea commodo consequat. Duis aute irure dolor in reprehenderit in voluptate velit esse cillum dolore eu fugiat nulla pariatur.</p>
    <p>Lorem ipsum dolor sit amet, consectetur adipisicing elit, sed do eiusmod tempor incididunt ut labore et dolore magna aliqua. Ut enim ad minim veniam, quis nostrud exercitation ullamco laboris nisi ut aliquip ex ea commodo consequat. Duis aute irure dolor in reprehenderit in voluptate velit esse cillum dolore eu</p>
  </div>
  <div class="brand panel-brand">KMaldrey Consulting</div>
</section>

<!-- Section title -->
<section class="slide c2 r3 section">
  <svg class="abs" style="left:0;top:0" width="357" height="276" viewBox="0 0 357 276">
    <circle cx="175" cy="146" r="22" fill="#fff"/>
    <circle cx="178" cy="134" r="3" fill="var(--blue)"/>
    <path d="M170 142 L179 141 L174 160 L179 158 L178 161 L168 162 L173 145 L169 145 Z" fill="var(--blue)"/>
    <line x1="125" y1="168" x2="227" y2="168" stroke="#cfe3f7" stroke-width=".8"/>
  </svg>
  <h2 class="abs section-title">SECTION TITLE</h2>
</section>

<!-- Close out -->
<section class="slide c3 r3" style="left:782px">
  <div class="cover-top"></div>
  <div class="brand close-brand">KMaldrey Consulting</div>
  <div class="ph" role="img" aria-label="Street map showing the office location by a lake" style="left:0;top:101px;width:357px;height:101px;background:linear-gradient(135deg,#e8e6df 0%,#d9dde0 45%,#a9c4de 55%,#e3e2dc 100%)"></div>
  <svg class="abs" style="left:0;top:190px" width="357" height="86" viewBox="0 0 357 86">
    <polygon points="226,0 280,0 270,12 214,12" fill="var(--grey)"/>
    <rect y="12" width="357" height="74" fill="var(--blue)"/>
    <g fill="#fff">
      <path d="M34 31 a4 4 0 1 1 8 0 c0 3 -4 7 -4 7 s-4 -4 -4 -7z"/>
      <rect x="34" y="50" width="8" height="6" rx="2"/>
      <rect x="34" y="68" width="8" height="8" rx="1.5"/>
      <rect x="139" y="30" width="9" height="7" rx="1.5"/>
      <circle cx="143.5" cy="57" r="4.5"/>
    </g>
  </svg>
  <div class="abs contact" style="left:52px;top:219px">4120 Harbor Ridge Blvd Ste 300<br>Lakeview, Texas 77001</div>
  <div class="abs contact" style="left:52px;top:242px">1.800.555.0142</div>
  <div class="abs contact" style="left:52px;top:260px">832.555.0179</div>
  <div class="abs contact" style="left:157px;top:222px">support@kmaldrey.com</div>
  <div class="abs contact" style="left:157px;top:244px">www.kmaldrey.com</div>
  <div class="abs socials" style="left:138px;top:259px"><span></span><span></span><span></span></div>
</section>

</main>
</body>
</html>
```